Activity List

We need a brochure designed for the Brackley House, which is a holiday villa in Sri Lanka. The brochure will be sent to travel agents and holiday travellers by email and also be printed and placed at the Brackley House. The brochure should be sophisticated yet indicate a sense of adventure.

```html
<!DOCTYPE html>
<html lang="en">
<head>
<meta charset="utf-8">
<title>Brackley House – Brochure Covers</title>
<link rel="stylesheet" href="https://fonts.googleapis.com/css2?family=Open+Sans:wght@400;600&display=swap">
<style>
  :root {
    --backdrop: #b7d6d7;
    --paper: #e8e8e4;
    --teal: #0898aa;
    --teal-light: #2bb3c2;
    --teal-dark: #07879a;
    --ink: #5f6466;
    --white: #ffffff;
    --frame-line: rgba(255,255,255,0.75);
    --logo-frame: #9aa2a3;
    --foliage-dark: #3a5a2a;
    --foliage-mid: #5a7d3c;
    --foliage-warm: #6e6a4c;
  }
  * { box-sizing: border-box; margin: 0; padding: 0; }
  html, body {
    width: 1200px; height: 700px; overflow: hidden;
    background: var(--backdrop);
    font-family: "Open Sans", sans-serif;
  }
  .spread {
    position: absolute; left: 40px; top: 152px;
    width: 1120px; height: 396px;
    display: flex;
    box-shadow: 0 10px 30px rgba(40,80,85,0.25);
  }
  .page { position: relative; width: 560px; height: 396px; background: var(--paper); overflow: hidden; }

  /* Back cover */
  .back-cover__field {
    position: absolute; inset: 16px;
    background: linear-gradient(100deg, var(--teal-light) 0%, var(--teal) 55%, var(--teal-dark) 100%);
  }
  .contact-band {
    position: absolute; left: 92px; top: 150px;
    width: 376px; height: 96px;
    background: var(--paper);
    display: flex; align-items: center;
  }
  .contact-band__name {
    width: 176px; text-align: center;
    color: var(--teal-dark);
    font-size: 12px; font-weight: 400; letter-spacing: 2.5px;
    text-transform: uppercase;
  }
  .contact-band__divider { width: 1px; height: 64px; background: var(--logo-frame); }
  .contact-list { list-style: none; padding-left: 16px; font-size: 8px; line-height: 1.45; color: var(--ink); }
  .contact-list li { display: flex; align-items: flex-start; gap: 5px; }
  .contact-list svg { flex: none; margin-top: 2px; }

  /* Front cover */
  .cover-photo {
    position: absolute; left: 0; top: 0; width: 370px; height: 396px;
    background: linear-gradient(170deg, var(--foliage-dark) 0%, var(--foliage-mid) 55%, var(--foliage-warm) 100%);
  }
  .tagline-frame {
    position: absolute; left: 180px; top: 150px; width: 170px; height: 60px;
    border: 1px solid var(--frame-line); border-right: none;
  }
  .tagline {
    position: absolute; left: 196px; top: 159px;
    font-size: 17px; line-height: 1.2; font-weight: 400;
  }
  .tagline__lead { color: var(--teal-light); display: block; }
  .tagline__rest { color: var(--white); display: block; }
  .cover-brand {
    position: absolute; left: 330px; top: 72px; width: 200px; height: 72px;
    border: 1px solid var(--logo-frame);
    display: flex; align-items: center; justify-content: flex-end; padding-right: 18px;
  }
  .cover-brand__name {
    color: var(--teal-dark);
    font-size: 11px; font-weight: 400; letter-spacing: 2.2px; text-transform: uppercase;
    background: var(--paper); padding: 4px 6px;
  }
  .cover-web {
    position: absolute; left: 386px; bottom: 22px;
    display: flex; align-items: center; gap: 5px;
    font-size: 7.5px; letter-spacing: 1.2px; color: var(--ink);
  }
  .cover-web__dot { width: 6px; height: 6px; border-radius: 50%; background: var(--teal); }
  .cover-tab { position: absolute; right: 0; bottom: 44px; width: 18px; height: 5px; background: var(--teal); }
</style>
</head>
<body>
  <main class="spread">
    <section class="page back-cover">
      <div class="back-cover__field"></div>
      <div class="contact-band">
        <div class="contact-band__name">Brackley House</div>
        <div class="contact-band__divider"></div>
        <ul class="contact-list">
          <li>
            <svg width="7" height="7" viewBox="0 0 10 10"><circle cx="5" cy="5" r="5" fill="#0898aa"/><circle cx="5" cy="4.2" r="1.6" fill="#fff"/></svg>
            <span>Brackley House<br>17/4 Riverbend Lane, Mistvale,<br>Sri Lanka. 3187</span>
          </li>
          <li>
            <svg width="7" height="7" viewBox="0 0 10 10"><circle cx="5" cy="5" r="5" fill="#0898aa"/><rect x="3.5" y="2.5" width="3" height="5" rx="0.6" fill="#fff"/></svg>
            <span>+94 81 555 0142</span>
          </li>
          <li>
            <svg width="7" height="7" viewBox="0 0 10 10"><circle cx="5" cy="5" r="5" fill="#0898aa"/><rect x="3.5" y="2.5" width="3" height="5" rx="0.6" fill="#fff"/></svg>
            <span>+94 60 555 0187</span>
          </li>
          <li>
            <svg width="7" height="7" viewBox="0 0 10 10"><circle cx="5" cy="5" r="5" fill="#0898aa"/><rect x="2.5" y="3.3" width="5" height="3.4" fill="#fff"/></svg>
            <span>stay@brackleyhouse.com</span>
          </li>
        </ul>
      </div>
    </section>

    <section class="page front-cover">
      <div class="cover-photo" role="img" aria-label="Photograph of a stone stairway climbing through a tropical garden towards the villa"></div>
      <div class="tagline-frame"></div>
      <h1 class="tagline">
        <span class="tagline__lead">Escape from the</span>
        <span class="tagline__rest">demands of city life</span>
      </h1>
      <div class="cover-brand"><span class="cover-brand__name">Brackley House</span></div>
      <div class="cover-web"><span class="cover-web__dot"></span>www.brackley-house.com</div>
      <div class="cover-tab"></div>
    </section>
  </main>
</body>
</html>
```